LRV Website

We need a completely new modern design for our website www.lrv.org.au.

The Tenure Holders Alliance of Australia Inc is a non-profit, volunteer-run association representing owners of strata-titled residential developments. We provide education, information and lobbying to improve the management of apartment complexes and the lives of those living in them. We’re all about “owners helping owners”. More information on our organisation can be seen at www.lrv.org.au.

Our new logo (from a recent MarkPanel contest) is attached.

Target Market(s)

Primary audience - Owners of residential apartments - both resident owners and investor owners
Secondary audiences – current and potential sponsors; organisations providing products & services to Owners Corporations & Body Corporates

Industry/Entity Type

Non-Profit

Number of Pages Required

3 pages

Requirements
Must have
• We need:
- A design for the home page
- A design for 2-column content pages
- Fonts and colours for
* standard text
* H1, H2, H3 and H4 heading tags
* Bulleted and numbered lists
- A complementary colour scheme for the Calendar page
- A complementary breadcrumb format
- A standard format to display the associated tags for any content page

The above are described in more detail in the attached document.

The design should:
- be modern, uncluttered and clean
- reflect a sense of community, coupled with authority, professionalism and knowledge
- be a fixed width of 1000px

At a minimum the files we need are:
- The source file (PSD with all component layers is preferred, but not mandatory)
- JPG preview files
- Any stand-alone images as a PNG with transparent backgrounds
- Details of all fonts and sizes used (if they can’t be easily identified in the source files)

Note: The site is built with the Drupal CMS, so all page elements must be able to be clearly isolated.
Should not have
• Any fonts that are not freely available

```html
<!DOCTYPE html>
<html lang="en">
<head>
<meta charset="utf-8">
<title>LRV — Website Design: Home, Content and Events Pages</title>
<link rel="stylesheet" href="https://fonts.googleapis.com/css2?family=Arimo:wght@400;700&family=Noto+Sans:wght@400;700&display=swap">
<style>
:root{
  --gold:#d6a131;
  --gold-dark:#b6841b;
  --gold-light:#e8bf5a;
  --blue:#0c3fa6;
  --blue-dark:#072a7a;
  --navy:#1d2f78;
  --link:#1b3a94;
  --page:#f4f4f4;
  --box:#e9e9e9;
  --text:#333;
  --dot:#b9b9b9;
  --cell:#e3e3e3;
  --cell-head:#8f8f8f;
}
*{box-sizing:border-box;margin:0;padding:0}
html,body{width:1200px;height:4147px;overflow:hidden;background:#fff}
body{position:relative;font-family:"Noto Sans",Verdana,sans-serif;color:var(--text);font-size:12px}
ul{list-style:none}
a{color:var(--link)}
.page{position:absolute;left:0;width:1200px}
.page-home{top:0;height:1377px}
.page-content{top:1425px;height:1300px}
.page-events{top:2790px;height:1300px}
.page-bg{position:absolute;left:24px;width:1155px;top:0;background:var(--page);border-left:1px solid #e2e2e2;border-right:1px solid #e2e2e2}
.abs{position:absolute}

/* header */
.brand{position:absolute;left:40px;top:14px;display:flex;align-items:center;gap:18px}
.brand-mark{width:118px;height:118px;background:var(--gold);display:block}
.brand-name{font-family:Arimo,Arial,sans-serif;font-size:31px;line-height:31px;letter-spacing:2px;color:var(--navy)}
.search{position:absolute;left:752px;top:40px;width:404px;height:89px;background:#fff;border:1px solid #e4e4e4;border-radius:4px;box-shadow:0 1px 3px rgba(0,0,0,.08)}
.search-input{position:absolute;left:13px;top:33px;width:278px;height:28px;border:1px solid #dcdcdc;background:#fff}
.search-btn{position:absolute;left:303px;top:33px;width:88px;height:28px;background:var(--blue);color:#fff;font-family:Arimo,Arial,sans-serif;font-size:20px;line-height:28px;text-align:center;border:none}
.mainnav{position:absolute;left:24px;top:156px;width:1155px;height:69px;background:linear-gradient(var(--gold-light),var(--gold) 45%,var(--gold-dark));border-bottom:3px solid #f2dba4;display:flex;align-items:center;padding-left:4px}
.mainnav li{font-family:Arimo,Arial,sans-serif;font-size:24px;color:#fff;padding:0 17px;border-right:1px solid rgba(255,255,255,.35);line-height:40px;text-shadow:0 1px 1px rgba(0,0,0,.2)}
.mainnav li:last-child{border-right:none}

/* footer */
.footer{position:absolute;left:24px;width:1155px;height:66px;background:linear-gradient(var(--gold-light),var(--gold) 40%,var(--gold-dark));color:#fff;font-size:13px;font-weight:700;text-align:center;line-height:66px;letter-spacing:.5px}

/* shared boxes */
.col-title{font-family:Arimo,Arial,sans-serif;color:var(--navy);font-size:21px;font-weight:400}
.panel{background:var(--box);border:2px solid #dadada;padding:16px}
.dots{position:absolute;width:0;border-left:2px dotted var(--dot)}
.topic-list li{font-size:11.5px;font-weight:700;color:#222;margin-bottom:15px;display:flex;align-items:center;gap:10px}
.topic-list li::before{content:"";width:9px;height:9px;background:var(--blue);flex:none}

/* home */
.hero{position:absolute;left:24px;top:229px;width:790px;height:209px;background:linear-gradient(#0d44b4,#0a37a0 70%,#072c86);border-bottom:3px solid var(--gold);padding:46px 22px;color:#fff;font-family:Arimo,Arial,sans-serif}
.hero p{font-size:22px;line-height:40px}
.hero b{font-weight:400;font-size:32px}
.hero-photo{position:absolute;left:822px;top:232px;width:362px;height:298px;background:linear-gradient(#3a4f8a 0%,#5f6a86 45%,#b9a24a 62%,#1c2440 80%,#3e3a1e);box-shadow:0 6px 14px rgba(0,0,0,.3);transform:skewY(-2deg)}
.login label{display:block;font-size:12px;font-weight:700;color:#222;margin-bottom:8px;letter-spacing:.5px}
.login .field{height:28px;background:#fff;border:1px solid #d8d8d8;margin-bottom:16px}
.login .btn{display:inline-block;background:var(--blue);color:#fff;font-weight:700;font-size:15px;padding:2px 14px;border:1px solid #06256d}
.login .small{font-size:10.5px;font-weight:700;margin-top:12px;color:#222}
.feature h2{font-family:Arimo,Arial,sans-serif;color:var(--blue);font-size:28px;font-weight:400;letter-spacing:-.5px;margin-bottom:14px}
.feature p{font-size:13.5px;line-height:17px;margin-bottom:16px;color:#444}
.readmore{font-size:12px;font-weight:700;text-decoration:underline;color:#222;text-align:right}
.news-box{background:linear-gradient(#fff,#ececec);border:1px solid #e0e0e0;padding:28px 14px}
.news-item h3{font-size:14px;font-weight:700;color:var(--link);text-decoration:underline;letter-spacing:.5px}
.news-item .meta{font-size:11px;font-weight:700;color:var(--link);margin:14px 0 18px}
.news-item p{font-size:13.5px;line-height:17px;color:#444;margin-bottom:12px}
.more-btn{display:inline-block;background:var(--gold);border:1px solid var(--gold-dark);font-size:11px;font-weight:700;color:#222;padding:2px 6px}
.news-sep{border-top:2px dotted #cfcfcf;margin:34px 0 32px}
.side-panel{background:var(--box);border:3px solid #dadada;padding:16px 12px}
.side-panel p{font-size:12px;line-height:15px;color:#444;margin-bottom:16px}
.side-panel p:last-child{margin-bottom:0}

/* content page */
.crumbs{position:absolute;left:24px;width:1155px;height:33px;background:#e8e8e8;border-top:2px solid #dddddd;font-size:11px;font-weight:700;color:var(--link);padding:9px 17px;display:flex;gap:8px}
.crumbs span+span::before{content:"";display:inline-block;width:7px;height:7px;background:var(--gold);margin-right:5px}
.side-title{font-size:17px;font-weight:700;color:var(--link)}
.article-list li{font-size:12px;font-weight:700;color:var(--link);letter-spacing:1px;margin-bottom:16px;display:flex;gap:11px;line-height:15px}
.article-list li::before{content:"";width:9px;height:9px;background:var(--gold);flex:none;margin-top:3px}
.article h2{font-size:19px;font-weight:400;color:var(--link);letter-spacing:1.5px;margin-bottom:12px}
.article p{font-size:13.5px;line-height:17px;color:#444;margin-bottom:16px}

/* events */
.view-tabs{display:flex;gap:38px;font-size:13.5px;font-weight:700;color:var(--link)}
.cal-bar{position:absolute;left:40px;top:341px;width:1100px;height:49px;background:linear-gradient(#1d52c0,var(--blue-dark));color:#fff;font-weight:700;font-size:13.5px;display:flex;justify-content:space-between;align-items:center;padding:0 14px;letter-spacing:1px}
.calendar{position:absolute;left:40px;top:390px;width:1100px;border-collapse:collapse;table-layout:fixed}
.calendar th{height:35px;background:linear-gradient(#a3a3a3,var(--cell-head));color:#fff;font-size:12.5px;letter-spacing:1px;border:1px solid #fff}
.calendar td{background:var(--cell);border:1px solid #fff;vertical-align:top;text-align:right;padding:4px 3px}
.calendar td.edge,.calendar th.edge{background:#dadada}
.day{display:inline-block;min-width:34px;background:#5577c6;color:#fff;font-size:12px;font-weight:700;text-align:center;padding:1px 4px}
.popup{position:absolute;left:491px;top:832px;width:327px;height:218px;background:#fff;border:2px solid #d2d2d2;box-shadow:0 3px 8px rgba(0,0,0,.18);padding:14px;font-size:12.5px;font-weight:700;color:#111;line-height:15px}
.popup h4{font-size:12.5px;color:var(--link);letter-spacing:.8px;margin-bottom:18px}
.popup .badge{position:absolute;right:24px;top:48px;width:44px;height:44px;border-radius:50%;background:#222}
.popup p{margin-bottom:14px}
</style>
</head>
<body>

<!-- ============ HOME PAGE ============ -->
<section class="page page-home">
  <div class="page-bg" style="height:1360px"></div>
  <div class="brand"><span class="brand-mark"></span><span class="brand-name">TENURE<br>HOLDERS<br>ALLIANCE</span></div>
  <div class="search"><div class="search-input"></div><div class="search-btn">Search</div></div>
  <ul class="mainnav"><li>Home</li><li>About</li><li>News</li><li>Events</li><li>Membership</li><li>Sponsorship</li><li>Links</li><li>Contact</li><li>Members Only</li></ul>

  <div class="hero">
    <p><b>Owners</b> Helping Owners</p>
    <p><b>Representing</b> Strata Title Residential Developments</p>
    <p><b>Lobbying and Sharing</b> Information to Improve Apartment Living</p>
  </div>
  <div class="hero-photo" role="img" aria-label="Photograph of apartment buildings lit at night reflected in the water"></div>

  <h2 class="col-title abs" style="left:37px;top:500px">Member Login</h2>
  <div class="panel login abs" style="left:43px;top:535px;width:257px;height:206px">
    <label>Username or e-mail: *</label><div class="field"></div>
    <label>Password: *</label><div class="field"></div>
    <span class="btn">LOGIN</span>
    <div class="small">Request new password</div>
  </div>

  <h2 class="col-title abs" style="left:37px;top:778px">Topic List</h2>
  <div class="panel abs" style="left:43px;top:813px;width:257px;height:185px;padding-top:16px">
    <ul class="topic-list">
      <li>Lorem ipsum.</li><li>Dolor sit amet, consectetur.</li><li>Adipisicing elit, sed do.</li>
      <li>Eiusmod tempor incididunt ut et.</li><li>Dolore magna aliqua.</li><li>Ut enim ad veniam, nostrud.</li>
    </ul>
  </div>

  <div class="dots" style="left:317px;top:504px;height:768px"></div>

  <div class="feature abs" style="left:330px;top:500px;width:520px">
    <h2>Featured Announcements</h2>
    <p>What happens when complaints get trampled underfoot. When is a bylaw not a bylaw? When the Residential Disputes Panel decides it doesn't really matter.</p>
    <p>Government reintroduce clamping and towing of illegally parked cars to stop protracted legal and sometimes physical disputes they say are turning apartment car parks into battle grounds</p>
    <div class="readmore">Read More...</div>
    <h2 style="margin-top:14px">Recent News</h2>
  </div>
  <div class="news-box abs" style="left:330px;top:760px;width:547px;height:480px">
    <div class="news-item">
      <h3>Bye bye to bylaws</h3>
      <div class="meta">Submitted by admin on 9 December 2009</div>
      <p>What happens when complaints get trampled underfoot. When is a bylaw not a bylaw? When the Residential Disputes Panel decides it doesn't really matter, that's when</p>
      <span class="more-btn">More...</span>
    </div>
    <div class="news-sep"></div>
    <div class="news-item">
      <h3>Push to clamp illegal parkers</h3>
      <div class="meta">Submitted by admin on 9 December 2009</div>
      <p>RESIDENTS in flats and other strata buildings are demanding the State Government reintroduce clamping and towing of illegally parked cars to stop protracted legal and sometimes physical disputes they say are turning apartment car parks into battle grounds</p>
      <span class="more-btn">More...</span>
    </div>
  </div>

  <div class="dots" style="left:885px;top:504px;height:768px"></div>

  <h2 class="col-title abs" style="left:902px;top:536px">Upcoming Events</h2>
  <div class="side-panel abs" style="left:902px;top:570px;width:260px;height:183px">
    <p>Lorem ipsum dolor sit amet, ceiusmod tempor incididunt ut labore et.</p>
    <p>Dolore magna aliqua. Ut enim ad minim veniam, quis nostrud.</p>
    <p>ExDuis aute irure dolor in repre-henderit in voluptate.</p>
  </div>
  <h2 class="col-title abs" style="left:902px;top:784px">Recent Forum Posts</h2>
  <div class="side-panel abs" style="left:902px;top:821px;width:260px;height:185px">
    <p>Lorem ipsum dolor sit amet, consectetur adipisicincididunt ut labore et.</p>
    <p>Dolore magna aliqua. Ut enim ad minim veniam, quis nostrud.</p>
    <p>Exercitation ullamcoe dolor in reprehenderit in voluptate.</p>
  </div>

  <div class="footer" style="top:1296px">©Tenure Holders Alliance Inc 2008 | Disclaimer | Contact Us</div>
</section>

<!-- ============ CONTENT PAGE ============ -->
<section class="page page-content">
  <div class="page-bg" style="height:1295px"></div>
  <div class="brand"><span class="brand-mark"></span><span class="brand-name">TENURE<br>HOLDERS<br>ALLIANCE</span></div>
  <div class="search"><div class="search-input"></div><div class="search-btn">Search</div></div>
  <ul class="mainnav" style="top:161px"><li>Home</li><li>About</li><li>News</li><li>Events</li><li>Membership</li><li>Sponsorship</li><li>Links</li><li>Contact</li><li>Members Only</li></ul>
  <div class="crumbs" style="top:233px"><span>Home</span><span>Members Area</span></div>

  <h3 class="side-title abs" style="left:40px;top:297px">Articles</h3>
  <ul class="article-list abs" style="left:48px;top:340px;width:330px">
    <li>Building Managements Rights-<br>Buyers Beware</li>
    <li>Building Owners &amp; Occupiers-<br>How Up to date must they be (FS 2217)</li>
    <li>Deffects</li>
    <li>Demistifying High-Rise Fire Safety</li>
    <li>Executive Committees</li>
    <li>Fire Safety and the new standrds<br>( FS 2217-2005 )</li>
    <li>Insurance Tips For Stats Plan</li>
    <li>Noise</li>
    <li>Owners Corporation &amp; GST</li>
    <li>Serviced Appartments- A New Form<br>Of Starta Abuse</li>
    <li>Smoke Alarms</li>
    <li>Strata Managers</li>
    <li>Which Way to Vote?<br>The Burden of Choice!</li>
  </ul>
  <h3 class="side-title abs" style="left:42px;top:843px;font-size:15px">Topic List</h3>
  <div class="panel abs" style="left:42px;top:877px;width:262px;height:186px">
    <ul class="topic-list">
      <li>Lorem ipsum.</li><li>Dolor sit amet, consectetur.</li><li>Adipisicing elit, sed do.</li>
      <li>Eiusmod tempor incididunt ut et.</li><li>Dolore magna aliqua.</li><li>Ut enim ad veniam, nostrud.</li>
    </ul>
  </div>

  <div class="dots" style="left:380px;top:298px;height:877px"></div>

  <div class="article abs" style="left:403px;top:297px;width:755px">
    <h2>Building Managements Rights- Buyers Beware</h2>
    <p>The Tenure Holders Alliance of Australia (LRV) is the peak body representing apartment owners, with most members drawn from Owners Corporations' Executive Committees (ECs) or concerned apartment owners around Australia. LRV is a not-for-profit association.</p>
    <p>Through representation, lobbying, information-sharing and networking, we perform a vital service for our members that supports them in living in and/or investing in strata titled property.</p>
    <p>We lobby for changes necessary to Government policy and legislation, and sit on many Government and industry boards and panels to present our views to those in power. The LRV gives members a voice at both State and Federal levels, and an opportunity to put forward their views on problems, solutions and the kind of future that, as apartment owners, we'd all like to see.</p>
  </div>
  <div class="article abs" style="left:403px;top:576px;width:755px">
    <h2>Building Owners &amp; Occupiers- How Up to date must they be (FS 2217)</h2>
    <p>The LRV educates EC members and individuals by sharing experiences and disseminating information from relevant sources and related organisations.</p>
    <p>Regular meetings, seminars and an online discussion group give members access to fellow members' experiences in areas such as defects rectification, strata disputes, shared services, and levy management. These resources may save members thousands of dollars and an immense amount of heartache in the long run!</p>
  </div>
  <div class="article abs" style="left:403px;top:788px;width:755px">
    <h2>Deffects</h2>
    <p>Regular meetings, seminars and an online discussion group give members access to fellow members' experiences in areas such as defects rectification, strata disputes, shared services, and levy management. These resources may save members thousands of dollars and an immense amount of heartache in the long run!</p>
  </div>
  <div class="article abs" style="left:403px;top:937px;width:755px">
    <h2>Demistifying High-Rise Fire Safety</h2>
    <p>Regular meetings, seminars and an online discussion group give members access to fellow members' experiences in areas such as defects rectification, strata disputes, shared services, and levy management. These resources may save members thousands of dollars and an immense amount of heartache in the long run!</p>
  </div>

  <div class="footer" style="top:1223px">©Tenure Holders Alliance Inc 2008 | Disclaimer | Contact Us</div>
</section>

<!-- ============ EVENTS PAGE ============ -->
<section class="page page-events">
  <div class="page-bg" style="height:1291px"></div>
  <div class="brand"><span class="brand-mark"></span><span class="brand-name">TENURE<br>HOLDERS<br>ALLIANCE</span></div>
  <div class="search"><div class="search-input"></div><div class="search-btn">Search</div></div>
  <ul class="mainnav" style="top:156px"><li>Home</li><li>About</li><li>News</li><li>Events</li><li>Membership</li><li>Sponsorship</li><li>Links</li><li>Contact</li><li>Members Only</li></ul>
  <div class="crumbs" style="top:230px"><span>Home</span><span>Events</span></div>

  <h3 class="side-title abs" style="left:39px;top:302px">Events</h3>
  <ul class="view-tabs abs" style="left:910px;top:320px"><li>Year</li><li>Month</li><li>Week</li><li>Day</li></ul>

  <div class="cal-bar"><span>« Prev</span><span>January 2010</span><span>Next »</span></div>
  <table class="calendar">
    <colgroup><col style="width:24px"><col style="width:137px"><col style="width:140px"><col style="width:144px"><col style="width:175px"><col style="width:164px"><col style="width:137px"><col style="width:179px"></colgroup>
    <thead><tr><th class="edge"></th><th>Sunday</th><th>Monday</th><th>Tuesday</th><th>Wednesday</th><th>Thursday</th><th>Friday</th><th>Saturday</th></tr></thead>
    <tbody>
      <tr style="height:82px"><td class="edge"></td><td></td><td></td><td></td><td></td><td></td><td><span class="day">1</span></td><td><span class="day">2</span></td></tr>
      <tr style="height:100px"><td class="edge"></td><td><span class="day">3</span></td><td><span class="day">4</span></td><td><span class="day">5</span></td><td><span class="day">6</span></td><td><span class="day">7</span></td><td><span class="day">8</span></td><td><span class="day">9</span></td></tr>
      <tr style="height:90px"><td class="edge"></td><td><span class="day">10</span></td><td><span class="day">11</span></td><td><span class="day">12</span></td><td><span class="day">13</span></td><td><span class="day">14</span></td><td><span class="day">15</span></td><td><span class="day">16</span></td></tr>
      <tr style="height:95px"><td class="edge"></td><td><span class="day">17</span></td><td><span class="day">18</span></td><td><span class="day">19</span></td><td><span class="day">20</span></td><td><span class="day">21</span></td><td><span class="day">22</span></td><td><span class="day">23</span></td></tr>
      <tr style="height:96px"><td class="edge"></td><td><span class="day">24</span></td><td><span class="day">25</span></td><td><span class="day">26</span></td><td><span class="day">27</span></td><td><span class="day">28</span></td><td><span class="day">29</span></td><td><span class="day">30</span></td></tr>
      <tr style="height:97px"><td class="edge"></td><td><span class="day">31</span></td><td></td><td></td><td></td><td></td><td></td><td></td></tr>
    </tbody>
  </table>

  <div class="popup">
    <h4>SPG Consumer Awareness Seminar</h4>
    <span class="badge"></span>
    <p>Time: 24 February 2010<br>6:15pm - 7:45pm</p>
    <p>Location:<br>Harbourline Conference Centre<br>48 Keel Street</p>
    <p>Sydney<br>Organiser: Strata Practice<br>Guild</p>
  </div>

  <div class="footer" style="top:1219px">©Tenure Holders Alliance Inc 2008 | Disclaimer | Contact Us</div>
</section>

</body>
</html>
```